Music Festival Business Cards

The Lantern Gathering
Produced by Bramblewood Sound Collective LLC
New music festival in Arkansas.

Target Market(s)

18-35 year olds

Industry/Entity Type

Festival

Contact Information for Business Card

We are a 5-partner team producing a music festival in Arkansas. We need slick business cards, and I want them to be square.

Requirements
Must have
• I NEED THESE TO BE IN SQUARE SIZE - 2x2 or 2.5x2.5... please not regular size.
• I need www.lanternmeet.example as the link to website.

```html
<!DOCTYPE html>
<html lang="en">
<head>
<meta charset="utf-8">
<title>The Lantern Gathering – Square Business Cards</title>
<link href="https://fonts.googleapis.com/css2?family=Tinos:wght@400;700&display=swap" rel="stylesheet">
<style>
  :root {
    --backdrop: #2f3040;
    --card-light: #3b3b3b;
    --card-dark: #050505;
    --frame-line: rgba(255, 255, 255, 0.38);
    --brand-grey: #8c8c8c;
    --brand-dim: #4a4a4a;
    --text-white: #ffffff;
    --accent-cyan: #35e3ee;
  }
  * { margin: 0; padding: 0; box-sizing: border-box; }
  html, body {
    width: 1200px; height: 840px; overflow: hidden;
    background: var(--backdrop);
  }
  .canvas { position: relative; width: 1200px; height: 840px; }
  .card {
    position: absolute; top: 206px;
    width: 426px; height: 426px;
    background: radial-gradient(ellipse at 40% 22%, var(--card-light) 0%, #1c1c1c 55%, var(--card-dark) 100%);
    font-family: "Tinos", "Times New Roman", serif;
  }
  .card-front { left: 139px; }
  .card-back { left: 650px; }
  .card-frame {
    position: absolute; inset: 16px;
    border: 1px solid var(--frame-line);
  }
  .front-brand {
    position: absolute; left: 0; right: 0; top: 150px;
    text-align: center;
    color: var(--brand-grey);
    font-weight: 700; font-size: 38px; line-height: 1.15;
    letter-spacing: 3px; text-transform: uppercase;
  }
  .back-brand {
    position: absolute; left: 0; right: 0; top: 118px;
    text-align: center;
    color: var(--brand-dim);
    font-weight: 700; font-size: 21px;
    letter-spacing: 2px; text-transform: uppercase;
  }
  .person { position: absolute; left: 43px; top: 198px; }
  .person-name { color: var(--text-white); font-size: 30px; line-height: 1.1; }
  .person-role { color: var(--accent-cyan); font-size: 18px; line-height: 1.2; }
  .contact-list { position: absolute; left: 43px; top: 272px; list-style: none; }
  .contact-item {
    display: flex; align-items: center; gap: 9px;
    color: var(--text-white); font-size: 20px; height: 32px;
  }
  .contact-icon { width: 16px; height: 16px; flex: none; }
</style>
</head>
<body>
<main class="canvas">
  <section class="card card-front" aria-label="Card front">
    <div class="card-frame"></div>
    <p class="front-brand">The Lantern<br>Gathering</p>
  </section>

  <section class="card card-back" aria-label="Card back">
    <div class="card-frame"></div>
    <p class="back-brand">The Lantern Gathering</p>
    <div class="person">
      <p class="person-name">Rowan Ellery</p>
      <p class="person-role">Service Manager</p>
    </div>
    <ul class="contact-list">
      <li class="contact-item">
        <svg class="contact-icon" viewBox="0 0 16 16" aria-hidden="true"><rect width="16" height="16" fill="#35e3ee"/><rect x="3" y="5" width="10" height="7" fill="none" stroke="#000" stroke-width="1.2"/><path d="M3 5 L8 9 L13 5" fill="none" stroke="#000" stroke-width="1.2"/></svg>
        hello@lanternmeet.example
      </li>
      <li class="contact-item">
        <svg class="contact-icon" viewBox="0 0 16 16" aria-hidden="true"><rect width="16" height="16" fill="#35e3ee"/><circle cx="8" cy="8" r="5" fill="none" stroke="#000" stroke-width="1.2"/><path d="M3 8 H13 M8 3 C5.5 6 5.5 10 8 13 M8 3 C10.5 6 10.5 10 8 13" fill="none" stroke="#000" stroke-width="1"/></svg>
        www.lanternmeet.example
      </li>
      <li class="contact-item">
        <svg class="contact-icon" viewBox="0 0 16 16" aria-hidden="true"><rect width="16" height="16" fill="#35e3ee"/><path d="M5 3 L7 5.5 L6 7 C6.8 8.6 7.6 9.4 9 10 L10.5 9 L13 11 L11.5 13 C7.5 12.5 3.5 8.5 3 4.5 Z" fill="#000"/></svg>
        555-014-2231
      </li>
      <li class="contact-item">
        <svg class="contact-icon" viewBox="0 0 16 16" aria-hidden="true"><rect width="16" height="16" fill="#35e3ee"/><rect x="5" y="2.5" width="6" height="11" rx="1" fill="none" stroke="#000" stroke-width="1.2"/><rect x="6.3" y="4" width="3.4" height="4.5" fill="#000"/></svg>
        555-014-7780
      </li>
    </ul>
  </section>
</main>
</body>
</html>
```